Bramble Café retail envelop design

This is a single serve coffee product for the adventurer consumer. The product is Fair Trade, Organic coffee grounds in a single serve pouch that can be used as a quality pour over drip brew while on the go. We would like to use designs that show adventure/hiking/camping with earth tones that display a organic/biodegradable feel.The open width of envelope film is 200mmThe finished bag size is W 100mm * L 120mm. (Once sealed)The eye mark size is W 10* H 5 mm. (side seam)Top/Bottom heat seal: 8mmSide heat seal: 7mmPlease use the samples provided as a guide only. I would like to see what you can come up with. Please use our original logo attached.Three blend varieties: Kelvermoor, Hollow, WarsawIG: @Bramblecafe

Target Market(s)

Adventurers, backpackers, campers, hikers, adventure riders, etc.

Colors

Designer to choose colors to be used in the design.

Requirements
Must have
• My Bramble Cafe logo, earthy feel (maybe black logo on earthy paper color backdrop?). Must show 12g size, instruction panel (this can be edited for visual appeal), IG account: Bramblecafe.
• Design will be printed in Matte finish.
Should not have
• It does not need all of the text that is shown on the back. I will prefer a more simplistic design rather than a crowded one.

```html
<!DOCTYPE html>
<html lang="en">
<head>
<meta charset="utf-8">
<title>Bramble Café – Single Serve Pouches</title>
<link rel="stylesheet" href="https://fonts.googleapis.com/css2?family=Montserrat:wght@800&family=Open+Sans:wght@600&family=Oswald:wght@700&display=swap">
<style>
  :root {
    --sky-bg: #42a6da;
    --sand-bg: #e9ca76;
    --ink: #231f20;
    --white: #ffffff;

    --hollow-top: #f2f9fe;
    --hollow-mid: #cfe9f8;
    --hollow-ridge: #8fcdf0;
    --hollow-slope: #3d93c8;
    --hollow-forest: #17557f;
    --hollow-ground: #0a2a40;
    --hollow-shadow: #030c13;
    --hollow-pill: #123a58;
    --hollow-pill-text: #a9d9f5;

    --kelvermoor-top: #fffaea;
    --kelvermoor-mid: #f7e3a6;
    --kelvermoor-ridge: #edc55c;
    --kelvermoor-slope: #c2901f;
    --kelvermoor-forest: #7a5810;
    --kelvermoor-ground: #3a2907;
    --kelvermoor-shadow: #0c0802;
    --kelvermoor-pill: #3a2707;
    --kelvermoor-pill-text: #f2a945;
  }

  * { box-sizing: border-box; margin: 0; padding: 0; }

  html, body {
    width: 1200px;
    height: 744px;
    overflow: hidden;
  }

  .stage {
    position: relative;
    width: 1200px;
    height: 744px;
    display: flex;
  }

  .backdrop--sky { width: 595px; height: 100%; background: var(--sky-bg); }
  .backdrop--sand { flex: 1; height: 100%; background: var(--sand-bg); }

  .pouch {
    position: absolute;
    top: 122px;
    width: 422px;
    height: 499px;
    overflow: hidden;
  }
  .pouch--hollow { left: 110px; }
  .pouch--kelvermoor { left: 670px; }

  .pouch__panel { position: absolute; inset: 0; }
  .pouch--hollow .pouch__panel {
    background: linear-gradient(180deg, var(--hollow-top) 0%, var(--hollow-mid) 60%, var(--hollow-mid) 100%);
  }
  .pouch--kelvermoor .pouch__panel {
    background: linear-gradient(180deg, var(--kelvermoor-top) 0%, var(--kelvermoor-mid) 60%, var(--kelvermoor-mid) 100%);
  }

  .pouch__scene {
    position: absolute;
    left: 0;
    right: 0;
    top: 248px;
    bottom: 0;
  }
  .pouch--hollow .pouch__scene {
    background: linear-gradient(180deg,
      rgba(143,205,240,0) 0%,
      var(--hollow-ridge) 10%,
      var(--hollow-slope) 28%,
      var(--hollow-forest) 50%,
      var(--hollow-ground) 72%,
      var(--hollow-shadow) 100%);
  }
  .pouch--kelvermoor .pouch__scene {
    background: linear-gradient(180deg,
      rgba(237,197,92,0) 0%,
      var(--kelvermoor-ridge) 10%,
      var(--kelvermoor-slope) 28%,
      var(--kelvermoor-forest) 50%,
      var(--kelvermoor-ground) 72%,
      var(--kelvermoor-shadow) 100%);
  }

  .pouch__seal-top {
    position: absolute;
    left: 0; right: 0; top: 0;
    height: 20px;
    background: repeating-linear-gradient(180deg, rgba(255,255,255,0.55) 0 2px, rgba(0,0,0,0.06) 2px 4px);
  }
  .pouch__seal-side {
    position: absolute;
    top: 0; bottom: 0;
    width: 18px;
    background: repeating-linear-gradient(90deg, rgba(255,255,255,0.3) 0 2px, rgba(0,0,0,0.05) 2px 4px);
  }
  .pouch__seal-side--left { left: 0; }
  .pouch__seal-side--right { right: 0; }

  .brand {
    position: absolute;
    left: 0; right: 0;
    top: 100px;
    text-align: center;
    font-family: "Oswald", sans-serif;
    font-weight: 700;
    color: var(--ink);
    line-height: 1;
  }
  .brand__name { display: block; font-size: 66px; letter-spacing: 1px; }
  .brand__sub { display: block; font-size: 42px; margin-top: 4px; }

  .variety {
    position: absolute;
    left: 0; right: 0;
    top: 320px;
    height: 56px;
    display: flex;
    align-items: center;
    justify-content: center;
    font-family: "Montserrat", sans-serif;
    font-weight: 800;
    color: var(--white);
    text-transform: uppercase;
    line-height: 1;
  }
  .variety--hollow { font-size: 52px; }
  .variety--kelvermoor { font-size: 32px; }

  .size-pill {
    position: absolute;
    left: 50%;
    top: 376px;
    transform: translateX(-50%);
    padding: 2px 10px;
    border-radius: 5px;
    font-family: "Open Sans", sans-serif;
    font-weight: 600;
    font-size: 16px;
    line-height: 19px;
    white-space: nowrap;
  }
  .pouch--hollow .size-pill { background: var(--hollow-pill); color: var(--hollow-pill-text); }
  .pouch--kelvermoor .size-pill { background: var(--kelvermoor-pill); color: var(--kelvermoor-pill-text); }
</style>
</head>
<body>
<main class="stage">
  <div class="backdrop--sky"></div>
  <div class="backdrop--sand"></div>

  <article class="pouch pouch--hollow">
    <div class="pouch__panel"></div>
    <div class="pouch__scene" role="img" aria-label="Adventure landscape in blue tones: mountain peaks with flying birds, forest, a hiker seated at a camp table drinking coffee beside a tent and lantern"></div>
    <div class="pouch__seal-top"></div>
    <div class="pouch__seal-side pouch__seal-side--left"></div>
    <div class="pouch__seal-side pouch__seal-side--right"></div>
    <h1 class="brand"><span class="brand__name">BRAMBLE</span><span class="brand__sub">Café</span></h1>
    <h2 class="variety variety--hollow">Hollow</h2>
    <p class="size-pill">12G SINGLE SERVE</p>
  </article>

  <article class="pouch pouch--kelvermoor">
    <div class="pouch__panel"></div>
    <div class="pouch__scene" role="img" aria-label="Adventure landscape in golden tones: mountain peaks with flying birds, forest, a hiker seated at a camp table drinking coffee beside a tent and lantern"></div>
    <div class="pouch__seal-top"></div>
    <div class="pouch__seal-side pouch__seal-side--left"></div>
    <div class="pouch__seal-side pouch__seal-side--right"></div>
    <h1 class="brand"><span class="brand__name">BRAMBLE</span><span class="brand__sub">Café</span></h1>
    <h2 class="variety variety--kelvermoor">Kelvermoor</h2>
    <p class="size-pill">12G SINGLE SERVE</p>
  </article>
</main>
</body>
</html>
```